Tuition Center Website

We need a new web site for a tutoring company based in sydney.

We only teach senior highschool students and pride ourselves on building the students abilities to think their way through life.

I would like a bright and vibrant website that looks professional and modern.
It needs to look simple and neat but also have the functionality we need.
Images and flash would be good.

Please keep in mind that the site must be appealing to a younger audience.

We need a multipage website with the following navigation bars:

1.Home (As logo not "home" button)
I would like a news box/ticker somewhere that can stream our chatterbook and peeplr feeds and also any news updates we want to put up.
Subscribe to newsletter button.

2. About us.
This needs to be a pull down into:
-What we do
-Why we do it
-How we do it

3. Courses
Pulldown into:
-Maths
-English
-Science
(we may need to attach extra pages behind these e.g. Courses/Science/Physics or Courses/Science/Chemistry and possibly add a link to a new formvik form)

4. Inspired
This page is like a blog page where we can upload videos, links to articles that we find to be inspiring and hopefully will inspire others.

5. Inspire
This is a recruitment page. Only content here.

6. Contact us.
Trovix map widget and a 'contact us' form

* Our branding requires green close to #12FF3D

***Please have a look at the current website.
@ www.velmoralearning.com.au

Thanks everybody hope the revision of my brief is better and more informative than my last one
Updates

Target Market(s)

senior highschool students aged 15-19, parents ( to a lesser degree)

Industry/Entity Type

It Company

Requirements
Must have
• Ability to change content on pages.

The green doesn't have to be everywhere, but it must be obvious that it is our colour.

Nice to have
• Sites with a nicer mix of images and flash will be given more consideration. But then again, if you amaze us, you amaze us and we will go with your design.
Should not have
• Should stay away from ocre, brown colours and serif fonts.

```html
<!DOCTYPE html>
<html lang="en">
<head>
<meta charset="utf-8">
<title>Velmora Learning</title>
<link rel="stylesheet" href="https://fonts.googleapis.com/css2?family=Carlito:wght@400;700&family=Arimo:wght@400&display=swap">
<style>
:root{
  --green:#62e000;
  --green-light:#9af55a;
  --green-deep:#4fc400;
  --ink:#1c1c1c;
  --icon:#3b3b3b;
  --white:#ffffff;
  --photo-a:#c9d4d6;
  --photo-b:#8a98a6;
}
*{margin:0;padding:0;box-sizing:border-box}
html,body{width:1050px;height:1200px;overflow:hidden;background:var(--white)}
body{position:relative;font-family:"Carlito",sans-serif;color:var(--ink)}
.abs{position:absolute}

.brand{left:74px;top:4px}
.brand-name{font-size:56px;color:var(--green);font-weight:700;letter-spacing:-1px;line-height:1}
.brand-tagline{font-size:21px;color:var(--ink);margin-top:4px;line-height:1}
.contact-top{right:74px;top:28px;text-align:right;font-size:21px;line-height:28px}
.contact-top .dot{display:inline-block;width:18px;height:18px;border-radius:50%;background:var(--icon);vertical-align:-2px;margin-right:6px}

.nav{left:0;top:90px;width:1050px;height:62px;background:linear-gradient(var(--green-light) 0 50%,var(--green) 50% 100%);box-shadow:0 3px 3px rgba(0,0,0,.45)}
.nav ul{list-style:none;display:flex;position:absolute;left:75px;top:12px;font-size:27px}
.nav li+li::before{content:"\\";margin:0 13px}

.hero{left:76px;top:168px;width:900px;height:357px;background:var(--green);padding:11px 12px;box-shadow:0 3px 4px rgba(0,0,0,.35)}
.hero-inner{position:relative;width:100%;height:100%;background:var(--white)}
.hero-mark{left:60px;top:19px;width:265px;height:207px;background:var(--green)}
.hero-name{left:20px;top:225px;width:330px;text-align:center;font-size:56px;line-height:50px;font-weight:700;color:var(--green)}
.hero-photo{left:384px;top:36px;width:465px;height:260px;background:linear-gradient(135deg,var(--photo-a),var(--photo-b))}
.hero-dots{left:752px;top:306px;display:flex;gap:10px}
.hero-dots span{width:12px;height:12px;border-radius:50%;background:var(--green)}
.hero-dots .on{width:15px;height:15px;margin-top:-1px;border:3px solid var(--ink);background:var(--green)}

.col{top:562px;width:285px}
.col h2{font-weight:400;font-size:27px;height:38px;padding:2px 14px;background:linear-gradient(var(--green-light) 0 78%,var(--green) 78% 100%)}
.col p{font-family:"Arimo",sans-serif;font-size:18px;line-height:22.5px;margin-top:13px}
.col-why{left:82px}.col-why p{padding:0 18px}
.col-trial{left:382px}.col-trial p{padding:0 20px;text-indent:46px}
.col-news{left:682px}.col-news p{padding:0 12px}
.col-news p+p{margin-top:5px}
.more{top:758px;width:123px;height:38px;font-size:21px;text-align:center;padding-top:9px;background:linear-gradient(var(--green-light) 0 80%,var(--green) 80% 100%)}

.tile{background:var(--green)}
.tile-big{top:805px;height:168px;background:linear-gradient(var(--green-light) 0 76%,var(--green) 76% 100%)}
.tile-big .label{position:absolute;right:18px;bottom:2px;font-size:27px}
.tile-big svg{position:absolute}
.tile-test{left:82px;width:302px}
.tile-feed{left:389px;width:297px}
.tile-social{left:691px;width:136px;height:82px;display:flex;align-items:center;justify-content:center;font-size:22px}
.tile-peeplr{top:805px}.tile-linkwise{top:892px}
.tile-login{left:832px;top:805px;width:136px;height:168px;font-size:36px;display:flex;align-items:center;justify-content:center}

.footer{left:0;top:1013px;width:1050px;height:187px;background:var(--green);font-size:14px}
.footer h3{font-size:14.5px;font-weight:700;margin-bottom:12px}
.foot-nav{left:115px;top:27px;line-height:19px}
.foot-nav ul{list-style:none}
.foot-sub{left:394px;top:27px}
.foot-sub .field{width:158px;height:22px;border:2px solid var(--ink);font-size:12.5px;font-style:italic;padding:1px 5px;margin-bottom:9px}
.foot-sub .btn{width:73px;height:20px;border:2px solid var(--ink);font-size:14px;text-align:center;line-height:16px}
.foot-addr{left:684px;top:27px;line-height:18.5px}
.foot-addr h3{margin-left:66px}
.foot-addr b{display:block}
.copy{left:0;width:1050px;top:1175px;text-align:center;font-size:12.5px}
</style>
</head>
<body>

<header>
  <div class="abs brand">
    <div class="brand-name">velmora learning</div>
    <div class="brand-tagline">inspiring minds nurturing potential equipping success</div>
  </div>
  <div class="abs contact-top">
    <div>For Inquire and contect</div>
    <div><span class="dot"></span>Phone: (02) 5550 3816</div>
  </div>
</header>

<nav class="abs nav">
  <ul><li>About Us</li><li>Courses</li><li>Inspired</li><li>Inspire</li><li>Contact us</li></ul>
</nav>

<section class="abs hero">
  <div class="hero-inner">
    <div class="abs hero-mark"></div>
    <div class="abs hero-name">velmora<br>learning</div>
    <div class="abs hero-photo" role="img" aria-label="Photo of five smiling senior students holding notebooks"></div>
    <div class="abs hero-dots"><span></span><span></span><span></span><span class="on"></span></div>
  </div>
</section>

<section class="abs col col-why">
  <h2>why velmora learning</h2>
  <p>Velmora Learning are HSC mentors and tutors who aim to build real relationships and offer you the help you need. HSC tutoring is different at Velmora – in a good way.</p>
</section>
<section class="abs col col-trial">
  <h2>free trial lession</h2>
  <p>Because we believe you shouldn't have to sign up until you see what it's actually like. Call or email us now!</p>
</section>
<section class="abs col col-news">
  <h2>latest news</h2>
  <p>Dt 25-JAN-2013<br>Year 11 Free HSC Workshops Starts now</p>
  <p>Dt 18-JAN-2013<br>Uni Open Days 2012</p>
</section>

<div class="abs more" style="left:163px">know more</div>
<div class="abs more" style="left:463px">know more</div>
<div class="abs more" style="left:763px">know more</div>

<div class="abs tile-big tile-test">
  <svg width="110" height="70" viewBox="0 0 110 70" style="left:96px;top:52px" fill="none" stroke="var(--icon)" stroke-width="5">
    <path d="M40 4h66v42H80l-10 10V46H40z"/>
    <path d="M4 20h66v42H34l-10 10V62H4z" fill="var(--green-light)"/>
  </svg>
  <span class="label">testimonials</span>
</div>
<div class="abs tile-big tile-feed">
  <svg width="110" height="90" viewBox="0 0 110 90" style="left:96px;top:42px" fill="var(--icon)">
    <rect x="0" y="22" width="40" height="40" rx="10"/>
    <polygon points="44,22 106,2 106,84 44,62"/>
    <rect x="12" y="62" width="26" height="24" rx="5"/>
  </svg>
  <span class="label">feedback</span>
</div>
<div class="abs tile tile-social tile-peeplr">peeplr</div>
<div class="abs tile tile-social tile-linkwise">linkwise</div>
<div class="abs tile tile-login">login</div>

<footer class="abs footer">
  <div class="abs foot-nav">
    <h3>Site Nevigation</h3>
    <ul><li>Home</li><li>About us</li><li>Courses</li><li>Inspired</li><li>Inspire</li><li>Contact us</li></ul>
  </div>
  <div class="abs foot-sub">
    <h3>Subscribe for latest update</h3>
    <div class="field">Enter your E-mail here</div>
    <div class="btn">Submit</div>
  </div>
  <div class="abs foot-addr">
    <h3>Address</h3>
    <b>Street:</b>48 Harlow St Ashvale NSW 2190
    <b>Phone:</b>(02) 5550 3816
    <b>Email:</b>learn@velmoralearning.com.au
  </div>
</footer>
<div class="abs copy">© copyright2013</div>

</body>
</html>
```